Need Bold, Hip Card for Concert Ticket Website Gleaming Passes!

Hi there! I am putting together a business/website that sells event tickets (mostly concerts, but also some sports and theater). Think SeatNook, but much smaller. The site is called Gleaming Passes. I have a new logo (attached, with black/red/white color scheme), and am looking for a modern/cool/original business card design. Note that I am thinking of having the card itself in the shape of a ticket (die cut), so you may want to keep that in mind when designing, but I'm not set on that. I'm also open to alternative card sizes, thicknesses, glossy, spot UV, etc. in order to stand out. I'm attaching a potential die cut template and a sample card using that template in case you want to work with that.
Target Market(s)
Music fans, people that like going to see live events
Industry/Entity Type
Entertainment
Contact Information for Business Card
Information that I'd like to have:
website address - www.gleamingpasses.example
phone number: 1-833-5GLEAMNG (532-6264)
my name - Wendel Pike

```html
<!DOCTYPE html>
<html lang="en">
<head>
<meta charset="utf-8">
<title>Gleaming Passes – Business Card</title>
<link rel="stylesheet" href="https://fonts.googleapis.com/css2?family=Montserrat:wght@800&family=Tinos&display=swap">
<style>
  :root {
    --backdrop: #c4c4c4;
    --card-red: #9b2c2e;
    --card-white: #f3f3f3;
    --brand-red: #ec1c2b;
    --ink: #111111;
    --foil: #1a1a1a;
  }
  * { margin: 0; padding: 0; box-sizing: border-box; }
  html, body { width: 1189px; height: 1200px; overflow: hidden; }
  body {
    position: relative;
    background: var(--backdrop);
    font-family: "Tinos", "Times New Roman", serif;
  }
  .ticket-card {
    position: absolute;
    left: 214px;
    width: 765px;
    height: 418px;
  }
  .ticket-card--front { top: 104px; }
  .ticket-card--back { top: 647px; }
  .ticket-card__shape {
    position: absolute;
    inset: 0;
    width: 100%;
    height: 100%;
  }
  .ticket-card--front .ticket-card__shape path { fill: var(--card-red); }
  .ticket-card--back .ticket-card__shape path { fill: var(--card-white); }
  .ticket-card__content {
    position: absolute;
    inset: 0;
    display: flex;
    flex-direction: column;
    align-items: center;
  }
  .ticket-card--front .ticket-card__content { justify-content: center; }
  .ticket-card--back .ticket-card__content { padding-top: 52px; }

  .brand {
    display: flex;
    align-items: center;
    gap: 18px;
  }
  .brand__mark {
    width: 64px;
    height: 64px;
  }
  .brand__name {
    font-family: "Montserrat", "Arial", sans-serif;
    font-weight: 800;
    font-size: 48px;
    line-height: 1.05;
    letter-spacing: 2px;
    text-transform: uppercase;
  }
  .brand--foil .brand__mark { background: var(--foil); }
  .brand--foil .brand__name { color: var(--foil); }
  .brand--print .brand__mark { background: var(--brand-red); }
  .brand--print .brand__name { color: var(--brand-red); }

  .contact__name {
    margin-top: 38px;
    font-size: 32px;
    color: var(--brand-red);
  }
  .contact__web {
    margin-top: 24px;
    font-size: 28px;
    color: var(--ink);
  }
  .contact__phone {
    margin-top: 22px;
    font-size: 26px;
    color: var(--ink);
  }
</style>
</head>
<body>

  <section class="ticket-card ticket-card--front" aria-label="Card front">
    <svg class="ticket-card__shape" viewBox="0 0 765 418" aria-hidden="true">
      <path d="M45 0 H720 A45 45 0 0 0 765 45 V373 A45 45 0 0 0 720 418 H45 A45 45 0 0 0 0 373 V45 A45 45 0 0 0 45 0 Z"/>
    </svg>
    <div class="ticket-card__content">
      <div class="brand brand--foil">
        <span class="brand__mark" aria-hidden="true"></span>
        <span class="brand__name">Gleaming<br>Passes</span>
      </div>
    </div>
  </section>

  <section class="ticket-card ticket-card--back" aria-label="Card back">
    <svg class="ticket-card__shape" viewBox="0 0 765 418" aria-hidden="true">
      <path d="M45 0 H720 A45 45 0 0 0 765 45 V373 A45 45 0 0 0 720 418 H45 A45 45 0 0 0 0 373 V45 A45 45 0 0 0 45 0 Z"/>
    </svg>
    <div class="ticket-card__content">
      <div class="brand brand--print">
        <span class="brand__mark" aria-hidden="true"></span>
        <span class="brand__name">Gleaming<br>Passes</span>
      </div>
      <p class="contact__name">Wendel Pike</p>
      <p class="contact__web">www.gleamingpasses.example</p>
      <p class="contact__phone">1-833-5GLEAMNG (532-6264)</p>
    </div>
  </section>

</body>
</html>
```